New Look Driving School Project

Current website:
www. kelmorawheelacademy.com

Websites that we like (use content and courses from here as well):
https://www. tollbenroadclass.com

We are looking for a fresh looking driving school website that is easy for students to find the course they are looking for, the price, and allow them to book a lesson all on our website. We would like for this website to have multiple pages: Home, Teen Courses, Adult Courses, About Us, Contact, FAQ, Blog, Requirements.

Target Market(s)

Students in High School or Parents

Industry/Entity Type

Education

Coding

Coded - Design and coding required

Number of Pages Required

5+ page

Font styles to use
Serif
Sans Serif

Colors

Designer to choose colors to be used in the design.

Requirements
Must have
• Must have a form submission and payment processing option. Must have the ability to pick a course, see available times, and process their payment online. MUST BE MOBILE FRIENDLY DESIGN.
Nice to have
• Nice to have a clean format, with big bold fonts.
Should not have
• Should not have a lot of sliders or animations. Should be very fast loading on mobile. Keep it simple but easy to read and elegant.

```html
<!DOCTYPE html>
<html lang="en">
<head>
<meta charset="utf-8">
<title>Kelmora Wheel Academy</title>
<link href="https://fonts.googleapis.com/css2?family=Mulish:wght@400;600;700;800;900&display=swap" rel="stylesheet">
<style>
:root{
  --red:#f2412f;
  --red-dark:#d8301f;
  --ink:#23252f;
  --navy:#2a2c37;
  --text:#444a55;
  --muted:#8a909a;
  --line:#dfe2e6;
  --mist:#d6dde4;
  --band:#e3e7eb;
  --white:#ffffff;
}
*{box-sizing:border-box;margin:0;padding:0}
html,body{width:1200px;height:4569px;overflow:hidden}
body{font-family:"Mulish",Arial,sans-serif;color:var(--text);background:var(--white);position:relative}
section,header,footer,nav{position:absolute;left:0;width:1200px}
.abs{position:absolute}
.btn{position:absolute;display:flex;align-items:center;justify-content:center;border-radius:20px;font-size:12px;font-weight:700}
.btn-red{background:var(--red);color:var(--white)}
.btn-ghost{border:1.5px solid var(--red);color:var(--red);background:var(--white)}
.arrow-sq{position:absolute;width:34px;height:34px;background:#e8ebee;display:flex;align-items:center;justify-content:center}
.arrow-sq.light{background:rgba(255,255,255,.85)}
.round-go{width:34px;height:34px;border-radius:50%;background:var(--red);display:flex;align-items:center;justify-content:center}

/* header */
.topbar{top:0;height:85px;background:var(--white)}
.brand{position:absolute;left:0;top:0;width:275px;height:85px;background:var(--red);clip-path:polygon(0 0,100% 0,86% 100%,0 100%);color:var(--white);font-weight:800;font-size:22px;line-height:23px;padding:18px 0 0 44px}
.call{position:absolute;left:378px;top:30px;font-size:15px;color:var(--text)}
.call b{color:var(--red);font-weight:800}
.hours{position:absolute;left:610px;top:33px;font-size:11px;color:var(--text);display:flex;align-items:center;gap:6px}
.top-btn{left:855px;top:24px;width:215px;height:36px}
.social{position:absolute;top:24px;width:34px;height:34px;border-radius:50%;background:#e9ecef}
.mainnav{top:85px;height:43px;background:var(--navy)}
.mainnav ul{list-style:none;display:flex;position:absolute;left:108px;top:0;height:43px}
.mainnav li{color:#d5d8de;font-size:12px;padding:0 26px;line-height:43px}
.mainnav li.on{background:var(--red);color:var(--white)}

/* hero */
.hero{top:128px;height:512px}
.hero-photo{position:absolute;inset:0;background:linear-gradient(100deg,#3b3530 0%,#7a6a5c 35%,#bcaa96 60%,#6d5f55 100%)}
.hero-shade{position:absolute;inset:0;background:linear-gradient(90deg,rgba(20,20,25,.7) 0%,rgba(20,20,25,.25) 50%,rgba(0,0,0,0) 80%)}
.hero h1{position:absolute;left:107px;top:150px;color:var(--white);font-size:37px;line-height:44px;font-weight:800}
.hero p{position:absolute;left:107px;top:247px;width:470px;color:#eef0f3;font-size:13px;line-height:19px}
.hero .btn{left:107px;top:318px;width:128px;height:34px;font-size:11px}

/* programs */
.programs{top:640px;height:685px;background:var(--white)}
.sec-title{position:absolute;left:0;width:1200px;text-align:center;color:var(--ink);font-weight:800;font-size:24px}
.sec-sub{position:absolute;left:0;width:1200px;text-align:center;font-size:12px;color:var(--muted)}
.card{position:absolute;top:128px;width:302px;height:435px;background:var(--white);box-shadow:0 6px 20px rgba(0,0,0,.08)}
.card .ph{height:213px;position:relative}
.price{position:absolute;left:0;bottom:0;width:150px;height:56px;background:var(--red);clip-path:polygon(0 0,100% 0,88% 100%,0 100%);color:var(--white);font-size:25px;font-weight:700;padding:12px 0 0 18px}
.price sup{font-size:13px}
.price small{font-size:18px;font-weight:600}
.card h3{font-size:15px;font-weight:800;color:var(--ink);margin:24px 0 0 24px}
.card p{font-size:11px;line-height:17px;color:var(--muted);margin:12px 24px 0;}
.card .foot{position:absolute;left:24px;top:362px;display:flex;gap:12px;align-items:center}
.card .book{position:static;width:76px;height:32px;font-size:10px}
.view{width:170px;height:36px}

/* find program */
.finder{top:1325px;height:515px;background:var(--navy)}
.finder-photo{position:absolute;left:0;top:0;width:680px;height:515px;clip-path:polygon(0 0,100% 0,72% 100%,0 100%);background:linear-gradient(110deg,#8b7060 0%,#c9a88f 40%,#6c6f78 75%,#3e414b 100%)}
.finder h2{position:absolute;left:560px;width:590px;top:40px;text-align:center;color:var(--white);font-size:26px;font-weight:800}
.finder .lead{position:absolute;left:560px;width:590px;top:78px;text-align:center;color:#b5b9c2;font-size:11px}
.field{position:absolute;height:38px;border:1px solid #555a67;color:#b9bdc6;font-size:11px;padding:0 12px;display:flex;align-items:center;justify-content:space-between}
.finder .btn{left:748px;top:426px;width:214px;height:36px;font-size:11px}

/* specialties */
.special{top:1840px;height:621px;background:var(--white)}
.spec{position:absolute;top:125px;width:302px}
.spec .frame{position:relative;height:182px;background:#e3e6ea}
.spec .frame .red{position:absolute;right:0;top:0;width:120px;height:182px;background:var(--red);clip-path:polygon(60% 0,100% 0,100% 100%,0 100%)}
.spec .frame .ph{position:absolute;left:30px;top:0;width:242px;height:182px;clip-path:polygon(18% 0,100% 0,82% 100%,0 100%)}
.spec h3{text-align:center;font-size:14px;font-weight:800;color:var(--ink);margin-top:26px;line-height:20px}
.spec p{text-align:center;font-size:11px;line-height:17px;color:var(--muted);margin:10px 30px 0}
.spec .go{margin:20px auto 0}

/* offer band */
.offer{top:2461px;height:129px;background:var(--band)}
.offer h2{position:absolute;left:107px;top:32px;font-size:27px;font-weight:700;color:var(--ink)}
.offer h2 span{color:var(--red);font-weight:800}
.offer p{position:absolute;left:107px;top:72px;font-size:12px;color:var(--text)}
.offer .cta{position:absolute;left:880px;top:0;width:320px;height:129px;background:var(--red);clip-path:polygon(14% 0,100% 0,100% 100%,0 100%);color:var(--white);font-weight:800;font-size:15px;display:flex;align-items:center;justify-content:center;padding-left:30px}

/* testimonials */
.testimony{top:2590px;height:517px}
.testimony .ph{position:absolute;inset:0;background:linear-gradient(90deg,#2c2e33 0%,#4a4b4f 45%,#7a7b80 70%,#3b3d43 100%)}
.testimony .shade{position:absolute;inset:0;background:rgba(25,26,32,.55)}
.testimony h2{position:absolute;left:0;width:1200px;top:50px;text-align:center;color:var(--white);font-size:24px;font-weight:800}
.quote-box{position:absolute;left:115px;top:130px;width:880px;height:230px}
.quote-box p{position:absolute;left:90px;top:30px;width:560px;font-size:15px;line-height:22px;color:#e4e6ea}
.name-tag{position:absolute;left:115px;top:343px;width:465px;height:77px;background:var(--red);clip-path:polygon(0 0,100% 0,88% 100%,0 100%)}
.avatar{position:absolute;left:25px;top:15px;width:47px;height:47px;border-radius:50%;background:#c9b6a5;border:2px solid var(--white)}
.name-tag b{position:absolute;left:88px;top:18px;color:var(--white);font-size:17px;font-weight:800}
.name-tag small{position:absolute;left:88px;top:42px;color:#ffe2de;font-size:11px}
.dots{position:absolute;left:555px;top:444px;display:flex;gap:8px}
.dots i{width:10px;height:10px;border-radius:50%;border:1.5px solid #d9dbe0}
.dots i.on{background:#d9dbe0}

/* features */
.features{top:3107px;height:381px;background:var(--mist)}
.feat{position:absolute;top:140px;width:230px;text-align:center}
.feat h3{font-size:13px;font-weight:800;color:var(--ink);margin-top:12px}
.feat p{font-size:10.5px;line-height:15px;color:var(--muted);margin-top:7px}
.features .btn{left:535px;top:310px;width:130px;height:34px;font-size:11px}

/* blog & faq */
.blogfaq{top:3488px;height:564px;background:var(--white)}
.col-title{position:absolute;top:54px;font-size:24px;font-weight:800;color:var(--ink)}
.post{position:absolute;top:131px;width:213px}
.post .ph{height:128px}
.post time{display:block;font-size:10px;color:var(--muted);margin-top:14px}
.post h4{font-size:14px;line-height:19px;font-weight:800;color:var(--ink);margin-top:8px}
.faq-open{position:absolute;left:625px;top:131px;width:465px}
.faq-q{display:flex;align-items:center;gap:12px;height:36px;padding:0 10px;font-size:13px;font-weight:800;color:var(--ink)}
.faq-open .faq-q{background:var(--navy);color:var(--white)}
.faq-a{border:1px solid var(--line);border-top:none;padding:14px 36px 16px;font-size:10.5px;line-height:16px;color:var(--muted)}
.faq-item{position:absolute;left:625px;width:465px;border-bottom:1px solid var(--line)}
.ico{width:16px;height:16px;border-radius:50%;background:var(--red);display:flex;align-items:center;justify-content:center;flex:none}
.ico.dark{background:var(--navy)}

/* cta band */
.flex-band{top:4052px;height:137px;background:var(--red)}
.flex-band h2{position:absolute;left:107px;top:38px;color:var(--white);font-size:25px;font-weight:800}
.flex-band p{position:absolute;left:107px;top:76px;color:#ffe0dc;font-size:13px}
.flex-band .cta{position:absolute;left:940px;top:0;width:260px;height:137px;background:var(--navy);clip-path:polygon(12% 0,100% 0,100% 100%,0 100%);color:var(--white);font-weight:800;font-size:15px;display:flex;align-items:center;justify-content:center;padding-left:20px}

/* footer */
.site-foot{top:4189px;height:380px;background:var(--navy);color:#a4a9b3}
.site-foot h5{position:absolute;top:56px;color:var(--white);font-size:14px;font-weight:800}
.site-foot ul{position:absolute;top:90px;list-style:none;font-size:11px;line-height:23px}
.foot-about{position:absolute;left:107px;top:90px;width:270px;font-size:11px;line-height:16px}
.foot-more{left:107px;top:178px;width:76px;height:28px;font-size:10px;border:1.5px solid var(--red);color:var(--red)}
.foot-call{position:absolute;left:790px;top:86px;font-size:23px;color:var(--white)}
.foot-call b{color:var(--red);font-weight:800}
.foot-hours{position:absolute;left:790px;top:120px;font-size:11px}
.foot-social{position:absolute;top:160px;width:30px;height:30px;border-radius:50%;background:#3c3f4b}
.foot-rule{position:absolute;left:107px;right:107px;top:290px;border-top:1px solid #3b3e4a}
.copy{position:absolute;left:107px;top:305px;font-size:10px;color:#858a95}
.foot-wedge{position:absolute;right:0;top:0;width:200px;height:380px;background:#30333f;clip-path:polygon(60% 0,100% 0,100% 100%,0 100%)}
</style>
</head>
<body>

<header class="topbar">
  <div class="brand">Kelmora Wheel<br>Academy</div>
  <div class="call">Call Now! <b>&#9990; 555-014-2870</b></div>
  <div class="hours">
    <svg width="12" height="12" viewBox="0 0 12 12"><circle cx="6" cy="6" r="5" fill="none" stroke="#444a55" stroke-width="1.3"/><path d="M6 3v3l2 1.5" fill="none" stroke="#444a55" stroke-width="1.3"/></svg>
    Mon - Sat 8:00 AM - 7:00 PM
  </div>
  <div class="btn btn-red top-btn">Schedule Your Driving Program</div>
  <div class="social" style="left:1090px"></div>
  <div class="social" style="left:1134px"></div>
</header>

<nav class="mainnav">
  <ul>
    <li class="on">Home</li><li>Teen Courses</li><li>Adult Courses</li><li>Faq's</li><li>Blog</li><li>About</li><li>Contact</li>
  </ul>
</nav>

<section class="hero">
  <div class="hero-photo" role="img" aria-label="Photo of a teen driver at the wheel with an instructor beside her"></div>
  <div class="hero-shade"></div>
  <h1>We are Experts in Teen<br>Driving Education</h1>
  <p>in Ashford, Millbrook, Dunmere, Halvern, Brayton, Oakhurst Corner, and the greater Westvale area.</p>
  <div class="btn btn-red">Contact Us Today!</div>
  <div class="arrow-sq light" style="left:35px;top:240px"><svg width="10" height="10" viewBox="0 0 10 10"><path d="M7 1L3 5l4 4" fill="none" stroke="#333" stroke-width="1.6"/></svg></div>
  <div class="arrow-sq light" style="left:1130px;top:240px"><svg width="10" height="10" viewBox="0 0 10 10"><path d="M3 1l4 4-4 4" fill="none" stroke="#333" stroke-width="1.6"/></svg></div>
</section>

<section class="programs">
  <h2 class="sec-title" style="top:52px">Choose Your Program</h2>
  <div class="sec-sub" style="top:90px">Pick a program that best fits your schedule and goals in our Driving School.</div>

  <article class="card" style="left:107px">
    <div class="ph" role="img" aria-label="Photo of a student driver's hands on the steering wheel" style="background:linear-gradient(135deg,#2d2f36,#6b6e76 60%,#a9abb0)"><div class="price"><sup>$</sup>250 <small>for</small></div></div>
    <h3>Behind the Wheel</h3>
    <p>Lorem ipsum dolor sit amet, consectetur adipiscing elit, sed do eiusmod tempor incididunt ut labore et dolore.</p>
    <div class="foot"><div class="round-go"><svg width="12" height="10" viewBox="0 0 12 10"><path d="M1 5h9M6 1l4 4-4 4" fill="none" stroke="#fff" stroke-width="1.6"/></svg></div><div class="btn btn-ghost book">Book Now</div></div>
  </article>
  <article class="card" style="left:450px">
    <div class="ph" role="img" aria-label="Photo of a young woman driving a private car" style="background:linear-gradient(135deg,#9aa6ad,#c9b9a8 50%,#6d7479)"><div class="price"><sup>$</sup>400 <small>for</small></div></div>
    <h3>Private Car Driving</h3>
    <p>Lorem ipsum dolor sit amet, consectetur adipiscing elit, sed do eiusmod tempor incididunt ut labore et dolore.</p>
    <div class="foot"><div class="round-go"><svg width="12" height="10" viewBox="0 0 12 10"><path d="M1 5h9M6 1l4 4-4 4" fill="none" stroke="#fff" stroke-width="1.6"/></svg></div><div class="btn btn-ghost book">Book Now</div></div>
  </article>
  <article class="card" style="left:792px">
    <div class="ph" role="img" aria-label="Photo of a smiling young man in the driver's seat" style="background:linear-gradient(135deg,#5d6a78,#b9a48f 55%,#44505c)"><div class="price"><sup>$</sup>600 <small>for</small></div></div>
    <h3>Adult Waiver Program</h3>
    <p>Lorem ipsum dolor sit amet, consectetur adipiscing elit, sed do eiusmod tempor incididunt ut labore et dolore.</p>
    <div class="foot"><div class="round-go"><svg width="12" height="10" viewBox="0 0 12 10"><path d="M1 5h9M6 1l4 4-4 4" fill="none" stroke="#fff" stroke-width="1.6"/></svg></div><div class="btn btn-ghost book">Book Now</div></div>
  </article>

  <div class="arrow-sq" style="left:35px;top:330px"><svg width="10" height="10" viewBox="0 0 10 10"><path d="M7 1L3 5l4 4" fill="none" stroke="#666" stroke-width="1.6"/></svg></div>
  <div class="arrow-sq" style="left:1130px;top:330px"><svg width="10" height="10" viewBox="0 0 10 10"><path d="M3 1l4 4-4 4" fill="none" stroke="#666" stroke-width="1.6"/></svg></div>
  <div class="btn btn-ghost view" style="left:515px;top:603px">View All Program</div>
</section>

<section class="finder">
  <div class="finder-photo" role="img" aria-label="Photo of a smiling student driver with an instructor holding a clipboard"></div>
  <h2>Find Driving Program</h2>
  <div class="lead">Send us your details and we'll find the best schedule for you!</div>
  <div class="field" style="left:618px;top:131px;width:225px">Enter your Name</div>
  <div class="field" style="left:868px;top:131px;width:222px">Email</div>
  <div class="field" style="left:618px;top:188px;width:225px">Phone</div>
  <div class="field" style="left:868px;top:188px;width:222px">Area / City</div>
  <div class="field" style="left:618px;top:243px;width:225px">Choose Course <svg width="8" height="6" viewBox="0 0 8 6"><path d="M0 0h8L4 6z" fill="#b9bdc6"/></svg></div>
  <div class="field" style="left:868px;top:243px;width:107px">Date <svg width="10" height="10" viewBox="0 0 10 10"><rect x="1" y="2" width="8" height="7" fill="none" stroke="#b9bdc6"/></svg></div>
  <div class="field" style="left:985px;top:243px;width:105px">Time <svg width="10" height="10" viewBox="0 0 10 10"><circle cx="5" cy="5" r="4" fill="none" stroke="#b9bdc6"/></svg></div>
  <div class="field" style="left:618px;top:283px;width:472px;height:104px;align-items:flex-start;padding-top:10px">Message ...</div>
  <div class="btn btn-red">Schedule Your Driving Program</div>
</section>

<section class="special">
  <h2 class="sec-title" style="top:55px">Kelmora Wheel Academy Specializes in:</h2>

  <div class="spec" style="left:107px">
    <div class="frame"><div class="red"></div><div class="ph" role="img" aria-label="Photo of a teen practising behind the wheel" style="background:linear-gradient(135deg,#3a3c42,#8d8f95 60%,#c4c2bf)"></div></div>
    <h3>Behind the Wheel for<br>Teens &amp; Adults</h3>
    <p>Lorem ipsum dolor sit amet, consectetur adipiscing elit, sed do eiusmod tempor incididunt ut labore et dolore magna aliqua.</p>
    <div class="round-go go"><svg width="12" height="10" viewBox="0 0 12 10"><path d="M1 5h9M6 1l4 4-4 4" fill="none" stroke="#fff" stroke-width="1.6"/></svg></div>
  </div>
  <div class="spec" style="left:450px">
    <div class="frame"><div class="red"></div><div class="ph" role="img" aria-label="Photo of a young man driving with the window down" style="background:linear-gradient(135deg,#c0b5a7,#8795a0 55%,#4d5863)"></div></div>
    <h3>Driver Improvement<br>Course</h3>
    <p>Lorem ipsum dolor sit amet, consectetur adipiscing elit, sed do eiusmod tempor incididunt ut labore et dolore magna aliqua.</p>
    <div class="round-go go" style="background:#fff;border:1px solid var(--line)"><svg width="10" height="10" viewBox="0 0 10 10"><path d="M5 1v8M1 5h8" stroke="#888" stroke-width="1.4"/></svg></div>
  </div>
  <div class="spec" style="left:792px">
    <div class="frame"><div class="red"></div><div class="ph" role="img" aria-label="Photo of a smiling learner holding a learner plate beside a red car" style="background:linear-gradient(135deg,#c2473a,#d9a98e 50%,#8c3a31)"></div></div>
    <h3>Driving Learners<br>Permits</h3>
    <p>Lorem ipsum dolor sit amet, consectetur adipiscing elit, sed do eiusmod tempor incididunt ut labore et dolore magna aliqua.</p>
    <div class="round-go go"><svg width="12" height="10" viewBox="0 0 12 10"><path d="M1 5h9M6 1l4 4-4 4" fill="none" stroke="#fff" stroke-width="1.6"/></svg></div>
  </div>

  <div class="arrow-sq" style="left:35px;top:200px"><svg width="10" height="10" viewBox="0 0 10 10"><path d="M7 1L3 5l4 4" fill="none" stroke="#666" stroke-width="1.6"/></svg></div>
  <div class="arrow-sq" style="left:1130px;top:200px"><svg width="10" height="10" viewBox="0 0 10 10"><path d="M3 1l4 4-4 4" fill="none" stroke="#666" stroke-width="1.6"/></svg></div>
  <div class="btn btn-ghost view" style="left:515px;top:540px">View All Program</div>
</section>

<section class="offer">
  <h2><span>Save 10%</span> Schedule your Driving Program Today!</h2>
  <p>Only this month! Book learning and receive a discount of 10%......not included packages</p>
  <div class="cta">Send Request</div>
</section>

<section class="testimony">
  <div class="ph" role="img" aria-label="Background photo of a young man seated in a car"></div>
  <div class="shade"></div>
  <h2>What Our People are Saying?</h2>
  <div class="quote-box">
    <svg class="abs" style="left:0;top:0" width="880" height="230" viewBox="0 0 880 230"><path d="M20 1H879L860 229H1Z" fill="none" stroke="rgba(255,255,255,.45)" stroke-width="1.5"/></svg>
    <p>Lorem ipsum dolor sit amet, consectetur adipiscing elit, sed do eiusmod tempor incididunt ut labore et dolore magna aliqua. Ut enim ad minim veniam, quis nostrud exercitation ullamco laboris nisi ut aliquip ex ea commodo consequat. Duis aute irure dolor in reprehenderit in voluptate velit esse ...</p>
    <svg class="abs" style="left:775px;top:115px" width="60" height="46" viewBox="0 0 60 46"><path d="M0 0h24v24L14 46H2l8-22H0zM34 0h24v24L48 46H36l8-22H34z" fill="#fff"/></svg>
  </div>
  <div class="name-tag">
    <div class="avatar" role="img" aria-label="Customer portrait"></div>
    <b>Lorem Ipsum Dummy</b><small>Dolor sit amet</small>
  </div>
  <div class="dots"><i class="on"></i><i></i><i></i><i></i><i></i></div>
  <div class="arrow-sq light" style="left:35px;top:260px"><svg width="10" height="10" viewBox="0 0 10 10"><path d="M7 1L3 5l4 4" fill="none" stroke="#333" stroke-width="1.6"/></svg></div>
  <div class="arrow-sq light" style="left:1130px;top:260px"><svg width="10" height="10" viewBox="0 0 10 10"><path d="M3 1l4 4-4 4" fill="none" stroke="#333" stroke-width="1.6"/></svg></div>
</section>

<section class="features">
  <h2 class="sec-title" style="top:50px">What out People are Saying?</h2>
  <div class="feat" style="left:98px">
    <svg width="30" height="26" viewBox="0 0 30 26"><path d="M5 11l3-8h14l3 8h3v10h-3v4h-4v-4H9v4H5v-4H2V11z" fill="#f2412f"/><circle cx="8" cy="16" r="2" fill="#d6dde4"/><circle cx="22" cy="16" r="2" fill="#d6dde4"/></svg>
    <h3>Affordable</h3>
    <p>You have nothing to worry about, as our services are affordable and flexible.</p>
  </div>
  <div class="feat" style="left:363px">
    <svg width="28" height="28" viewBox="0 0 28 28"><path d="M2 12h6v14H2zM10 12l5-10c3 0 4 2 3 5l-1 4h7c2 0 3 2 2 4l-3 9c-1 2-2 2-4 2H10z" fill="#f2412f"/></svg>
    <h3>Guarantee</h3>
    <p>You have nothing to worry about, as our services are affordable and flexible.</p>
  </div>
  <div class="feat" style="left:610px">
    <svg width="26" height="28" viewBox="0 0 26 28"><circle cx="13" cy="8" r="7" fill="#f2412f"/><path d="M1 28c0-8 5-12 12-12s12 4 12 12z" fill="#f2412f"/></svg>
    <h3>Experience</h3>
    <p>You have nothing to worry about, as our services are affordable and flexible.</p>
  </div>
  <div class="feat" style="left:869px">
    <svg width="28" height="28" viewBox="0 0 28 28"><path d="M14 1l4 9 9 1-7 6 2 10-8-5-8 5 2-10-7-6 9-1z" fill="#f2412f"/></svg>
    <h3>Certified</h3>
    <p>You have nothing to worry about, as our services are affordable and flexible.</p>
  </div>
  <div class="btn btn-red">Contact Us Today!</div>
</section>

<section class="blogfaq">
  <h2 class="col-title" style="left:107px">Latest Blog</h2>
  <article class="post" style="left:107px">
    <div class="ph" role="img" aria-label="Photo of hands gripping a steering wheel" style="background:linear-gradient(135deg,#2f3136,#7e7a74 60%,#b9b2a8)"></div>
    <time>25 Apr, 2018</time>
    <h4>Lorem Ipsum has been the industry's standard dummy text ever</h4>
  </article>
  <article class="post" style="left:365px">
    <div class="ph" role="img" aria-label="Photo of a young woman driving in sunlight" style="background:linear-gradient(135deg,#6f8fb0,#e0c3a1 55%,#8a6a55)"></div>
    <time>25 Apr, 2018</time>
    <h4>Lorem Ipsum has been the industry's standard</h4>
  </article>
  <div class="btn btn-ghost" style="left:107px;top:497px;width:95px;height:32px;font-size:10px">View All</div>

  <h2 class="col-title" style="left:625px">Frequently Asked Questions</h2>
  <div class="faq-open">
    <div class="faq-q"><span class="ico"><svg width="8" height="2" viewBox="0 0 8 2"><rect width="8" height="2" fill="#fff"/></svg></span>How long is the road test appointment?</div>
    <div class="faq-a">Yes you can, your parent or guardian must sign the form MV-44. Also, Westvale Motor Vehicles requires at least 50 hours of supervised training (of 15 hours must be night driving) in order to take your Road Test.</div>
  </div>
  <div class="faq-item" style="top:298px"><div class="faq-q"><span class="ico dark"><svg width="8" height="8" viewBox="0 0 8 8"><path d="M4 0v8M0 4h8" stroke="#fff" stroke-width="2"/></svg></span>I'm 16 years old, can I get my Driver License?</div></div>
  <div class="faq-item" style="top:346px"><div class="faq-q"><span class="ico dark"><svg width="8" height="8" viewBox="0 0 8 8"><path d="M4 0v8M0 4h8" stroke="#fff" stroke-width="2"/></svg></span>How do I obtain a Westvale CDL?</div></div>
  <div class="faq-item" style="top:394px"><div class="faq-q"><span class="ico dark"><svg width="8" height="8" viewBox="0 0 8 8"><path d="M4 0v8M0 4h8" stroke="#fff" stroke-width="2"/></svg></span>What is the process for getting my class?</div></div>
  <div class="btn btn-ghost" style="left:625px;top:497px;width:95px;height:32px;font-size:10px">View All</div>
</section>

<section class="flex-band">
  <h2>We offer very FLEXIBLE schedules and timings for you.</h2>
  <p>Send us your information and we will call or email to schedule!</p>
  <div class="cta">Contact Now!</div>
</section>

<footer class="site-foot">
  <div class="foot-wedge"></div>
  <h5 style="left:107px">Kelmora Wheel Academy</h5>
  <p class="foot-about">Lorem ipsum dolor sit amet, consectetur adipiscing elit, sed do eiusmod tempor incididunt ut labore et dolore magna aliqua. Ut enim ad minim veniam, quis nostrud exercitation.</p>
  <div class="btn foot-more">Read All</div>
  <h5 style="left:450px">Quick Link</h5>
  <ul style="left:450px"><li>About</li><li>Teen Courses</li><li>Adult Courses</li><li>Faq's</li><li>Blog</li><li>Contact</li></ul>
  <ul style="left:620px"><li>Term &amp; Condition</li><li>Privacy Policy</li><li>Sitemap</li></ul>
  <h5 style="left:790px">Need help? Contact Us!</h5>
  <div class="foot-call">Call. <b>555-014-2870</b></div>
  <div class="foot-hours">&#9719; Mon - Sat 8:00 AM - 7:00 PM</div>
  <div class="foot-social" style="left:790px"></div>
  <div class="foot-social" style="left:830px"></div>
  <div class="foot-rule"></div>
  <div class="copy">Copyright © 2018 Kelmora Wheel Academy, All Rights Reserved.</div>
</footer>

</body>
</html>
```